Quellin Rebranded Website boutique fitness studio

Looking for a simple, easy to navigate, aesthetically pleasing update of our rebranded website

Target Market(s)

Stay at home moms, discretionary income, fitness and wellness

Coding

Coded - Design and coding required

Number of Pages Required

1 page

Font styles to use
Sans Serif

Colors
0054AA
0677BA
7BADD7
CADEEF
E8F1F8

Requirements
Must have
• Instagram feed linked, "as seen in" banner, spot for studio video at a later date

```html
<!DOCTYPE html>
<html lang="en">
<head>
<meta charset="utf-8">
<title>Quellin — Elevated strength, for every body</title>
<link rel="stylesheet" href="https://fonts.googleapis.com/css2?family=Quicksand:wght@300;400;500&family=Work+Sans:wght@400;500;600&display=swap">
<style>
:root{
  --brand:#0054AA;
  --brand-deep:#00428a;
  --ocean:#0677BA;
  --sky:#7BADD7;
  --mist:#CADEEF;
  --ice:#E8F1F8;
  --ink:#3f4a5c;
  --muted:#6f7a8a;
  --white:#ffffff;
}
*{box-sizing:border-box;margin:0;padding:0}
html,body{width:1200px;height:3810px;overflow:hidden}
body{font-family:"Work Sans",sans-serif;color:var(--ink);background:var(--white);font-size:10px}
.wrap{width:880px;margin:0 auto;position:relative}
.eyebrow{font-size:7.5px;letter-spacing:3px;text-transform:uppercase;font-weight:500;color:var(--muted)}
h1,h2,h3{font-family:"Quicksand",sans-serif;font-weight:300;color:var(--brand)}
h2{font-size:30px;line-height:1.02;letter-spacing:-.3px}
.btn{display:inline-block;border-radius:20px;font-size:7.5px;letter-spacing:2.5px;text-transform:uppercase;font-weight:600;padding:9px 18px;white-space:nowrap}
.btn-light{background:var(--white);color:var(--brand)}
.btn-ghost{border:1px solid rgba(255,255,255,.8);color:var(--white)}
.btn-outline{border:1px solid var(--ocean);color:var(--ocean)}

/* hero */
.hero{position:relative;height:570px;color:var(--white);overflow:hidden}
.hero-photo{position:absolute;inset:0;background:linear-gradient(110deg,#0a2a5e 0%,#0d3b78 35%,#1a4f8f 60%,#0b3a75 80%,#0a2f66 100%)}
.hero-shade{position:absolute;inset:0;background:linear-gradient(90deg,rgba(0,25,60,.55),rgba(0,25,60,.15) 60%,rgba(0,25,60,0))}
.nav{position:absolute;top:0;left:0;right:0;height:52px}
.brand{position:absolute;left:160px;top:8px;color:var(--white)}
.brand-name{font-family:"Quicksand",sans-serif;font-weight:400;font-size:22px;letter-spacing:.5px;display:block}
.brand-tag{font-size:4.5px;letter-spacing:1px;text-transform:uppercase;display:block;margin-top:1px}
.nav-links{position:absolute;left:372px;top:21px;display:flex;gap:27px;font-size:7.5px;letter-spacing:2px;font-weight:600;text-transform:uppercase}
.nav-cta{position:absolute;right:160px;top:13px}
.hero-copy{position:absolute;left:160px;top:278px;width:440px}
.hero-copy .eyebrow{color:rgba(255,255,255,.85)}
.hero h1{color:var(--white);font-size:46px;line-height:1.02;margin:14px 0 16px;letter-spacing:-.3px}
.hero p{font-size:11px;line-height:1.6;width:350px;opacity:.95}
.hero-actions{margin-top:24px;display:flex;gap:12px}

/* offer band */
.offer{background:var(--brand);height:102px;color:var(--white)}
.offer .wrap{height:102px;display:flex;align-items:center;justify-content:space-between}
.offer .eyebrow{color:rgba(255,255,255,.8);font-size:6.5px}
.offer-title{font-family:"Quicksand",sans-serif;font-size:18px;margin:4px 0 3px}
.offer small{font-size:8px;opacity:.85}

/* press */
.press{height:103px;text-align:center;padding-top:24px;overflow:hidden;border-bottom:1px solid var(--mist)}
.press .eyebrow{font-size:6.5px}
.press-row{display:flex;gap:40px;white-space:nowrap;margin-top:14px;margin-left:-30px;font-family:"Quicksand",sans-serif;font-size:18px;color:var(--sky)}

/* about */
.about{height:680px}
.about .wrap{height:680px}
.about-copy{position:absolute;left:0;top:172px;width:440px}
.about h2{margin:12px 0 18px}
.about p{font-size:9.5px;line-height:1.75;color:var(--ink);width:310px}
.feature-grid{display:grid;grid-template-columns:215px 215px;gap:28px 0;margin-top:34px}
.feature h4{font-size:6.5px;letter-spacing:2.5px;color:var(--ocean);font-weight:600;text-transform:uppercase;margin-bottom:8px}
.feature p{font-size:8px;line-height:1.7;color:var(--muted);width:200px}
.studio-video{position:absolute;right:0;top:80px;width:415px;height:520px;border-radius:16px;background:linear-gradient(160deg,#0a2f66,#0677BA 50%,#7BADD7 85%,#0a2f66);display:flex;align-items:center;justify-content:center}
.studio-video svg{width:64px;height:64px}

/* experience */
.experience{background:var(--ice);height:373px;padding-top:72px}
.experience h2{margin-top:12px}
.pillars{display:grid;grid-template-columns:repeat(4,1fr);gap:20px;margin-top:42px}
.pillar svg{width:18px;height:18px;stroke:var(--ocean);fill:none;stroke-width:1.4}
.pillar h3{font-size:12px;font-weight:400;color:var(--ocean);margin:11px 0 9px}
.pillar p{font-size:8px;line-height:1.75;color:var(--muted)}

/* studios */
.studios{height:766px;padding-top:72px}
.studios h2{margin-top:12px}
.studio-grid{display:grid;grid-template-columns:430px 430px;gap:20px;margin-top:36px}
.studio{background:var(--brand);border-radius:16px;overflow:hidden;height:435px;color:var(--white)}
.studio-photo{height:287px}
.studio-photo.one{background:linear-gradient(150deg,#0a2a5e,#0677BA 50%,#7BADD7 80%,#0a2f66)}
.studio-photo.two{background:linear-gradient(150deg,#0a2a5e,#0d4a90 45%,#5a92c8 75%,#0a2a5e)}
.studio-info{padding:25px}
.studio-info .eyebrow{color:rgba(255,255,255,.8);font-size:6.5px}
.studio-info h3{color:var(--white);font-size:15px;font-weight:400;margin:10px 0 7px}
.studio-info small{font-size:7.5px;opacity:.8}
.studio-actions{display:flex;align-items:center;gap:12px;margin-top:18px}
.studio-actions .link{font-size:7px;letter-spacing:2.5px;text-transform:uppercase;opacity:.85}
.coming{margin-top:20px;border:1px solid var(--mist);border-radius:14px;height:52px;display:flex;align-items:center;justify-content:center;gap:26px;font-size:7.5px}
.coming .eyebrow{font-size:6.5px;color:var(--sky)}
.coming b{color:var(--brand);font-weight:600}

/* testimonials */
.love{background:var(--ice);height:421px;padding-top:72px}
.love h2{margin-top:12px}
.quotes{display:grid;grid-template-columns:repeat(3,1fr);gap:18px;margin-top:38px}
.quote{background:var(--white);border-radius:14px;height:153px;padding:22px 20px}
.quote .mark{font-family:"Quicksand",sans-serif;color:var(--sky);font-size:16px;line-height:1}
.quote p{font-size:8.5px;line-height:1.75;color:var(--brand);margin:10px 0 14px}
.quote cite{font-style:normal;font-size:6.5px;letter-spacing:2.5px;color:var(--ocean);font-weight:600}

/* instagram */
.social{height:360px;padding-top:72px}
.social-head{display:flex;justify-content:space-between;align-items:flex-end}
.social h2{margin-top:12px}
.tiles{display:grid;grid-template-columns:repeat(6,1fr);gap:8px;margin-top:30px}
.tile{height:140px}
.t1{background:linear-gradient(160deg,#0a2a5e,#7BADD7,#0d3b78)}
.t2{background:#123a66}
.t3{background:linear-gradient(160deg,#0a2a5e,#CADEEF,#0d3b78)}
.t4{background:linear-gradient(170deg,#0a2f66,#0677BA)}
.t5{background:linear-gradient(160deg,#0a2a5e,#0054AA,#0a2040)}
.t6{background:#0677BA}

/* newsletter */
.newsletter{background:var(--brand);height:160px;color:var(--white)}
.newsletter .wrap{height:160px;display:flex;align-items:center;justify-content:space-between}
.newsletter .eyebrow{color:rgba(255,255,255,.8);font-size:6.5px}
.newsletter h2{color:var(--white);font-size:22px;margin:8px 0 4px}
.newsletter small{font-size:8px;opacity:.85}
.signup{display:flex;gap:8px}
.field{width:195px;height:30px;border:1px solid rgba(255,255,255,.45);border-radius:16px;font-size:8px;padding:9px 14px;color:rgba(255,255,255,.75)}

/* footer */
.footer{background:var(--brand-deep);height:275px;color:rgba(255,255,255,.88);padding-top:52px}
.footer-grid{display:grid;grid-template-columns:228px 228px 228px 196px;font-size:8px;line-height:1.7}
.footer .brand-name{font-family:"Quicksand",sans-serif;font-size:24px;display:block}
.footer .brand-tag{font-size:5px;letter-spacing:1px;text-transform:uppercase;display:block}
.footer-about{margin-top:16px;width:195px}
.social-icons{display:flex;gap:12px;margin-top:12px}
.social-icons span{width:10px;height:10px;border:1px solid rgba(255,255,255,.8);border-radius:2px}
.social-icons span+span{border-radius:50%}
.footer h5{font-size:6.5px;letter-spacing:2.5px;font-weight:500;opacity:.65;margin-bottom:14px}
.footer ul{list-style:none}
.footer li{margin-bottom:5px}
.legal{margin-top:58px;border-top:1px solid rgba(255,255,255,.15);padding-top:14px;display:flex;justify-content:space-between;font-size:6.5px;opacity:.65}
.legal span+span{margin-left:14px}
</style>
</head>
<body>

<header class="hero">
  <div class="hero-photo" role="img" aria-label="Instructor coaching a class in the studio under blue lighting"></div>
  <div class="hero-shade"></div>
  <nav class="nav">
    <div class="brand"><span class="brand-name">Quellin</span><span class="brand-tag">Elevated strength.</span></div>
    <div class="nav-links"><span>Schedule</span><span>Pricing</span><span>The Studio</span><span>Instructors</span><span>Contact</span></div>
    <a class="btn btn-ghost nav-cta">Claim intro offer</a>
  </nav>
  <div class="hero-copy">
    <div class="eyebrow">Marrow Creek, TX · West Alder, TX</div>
    <h1>Elevated strength, for every body.</h1>
    <p>A boutique Tensa studio and close-knit community, built to eliminate the intimidation of workout classes and gently push you beyond limits — one 40-minute class at a time.</p>
    <div class="hero-actions"><a class="btn btn-light">Claim intro offer</a><a class="btn btn-ghost">View schedule</a></div>
  </div>
</header>

<section class="offer">
  <div class="wrap">
    <div>
      <div class="eyebrow">New client offer</div>
      <div class="offer-title">2 Weeks Unlimited for $89</div>
      <small>Every class, every instructor — no commitment required. <em>[Studio to confirm final offer terms]</em></small>
    </div>
    <a class="btn btn-light">Book your intro class</a>
  </div>
</section>

<section class="press">
  <div class="eyebrow">The Tensa method, as seen in</div>
  <div class="press-row"><span>Daily Ledger</span><span>Brightwell</span><span>Vital Men</span><span>Lumière</span><span>Form</span><span>Folks Weekly</span><span>Thrive+Co</span><span>Poise</span><span>Roam Noir</span><span>Daily Ledger</span><span>Brightwell</span></div>
</section>

<section class="about">
  <div class="wrap">
    <div class="about-copy">
      <div class="eyebrow">What is Tensa</div>
      <h2>Low-impact.<br>High-intensity.<br>Real results.</h2>
      <p>We believe strength is for everyone. Quellin is a close-knit, female-owned studio where workouts go beyond routine — every class is designed to challenge, empower and keep you coming back, in an environment that feels welcoming from the moment you walk in.</p>
      <div class="feature-grid">
        <div class="feature"><h4>Full body</h4><p>One 40-minute Tensaformer class works nearly every muscle group.</p></div>
        <div class="feature"><h4>Joint-friendly</h4><p>Spring-based resistance builds strength without the impact.</p></div>
        <div class="feature"><h4>Instructor-led</h4><p>Hands-on form cues in every class, every time — no exceptions.</p></div>
        <div class="feature"><h4>Female-owned</h4><p>Built by women, for a community that believes in strength through movement.</p></div>
      </div>
    </div>
    <div class="studio-video" role="img" aria-label="Studio video placeholder: a class on Tensaformer machines">
      <svg viewBox="0 0 64 64"><circle cx="32" cy="32" r="30" fill="none" stroke="#ffffff" stroke-width="2"/><path d="M26 21v22l18-11z" fill="#ffffff"/></svg>
    </div>
  </div>
</section>

<section class="experience">
  <div class="wrap">
    <div class="eyebrow">The Quellin experience</div>
    <h2>Everything you need for<br>your first class — and<br>every one after.</h2>
    <div class="pillars">
      <div class="pillar">
        <svg viewBox="0 0 20 20"><path d="M10 17 3.5 10.5a3.8 3.8 0 0 1 6.5-4 3.8 3.8 0 0 1 6.5 4Z"/></svg>
        <h3>Judgment-Free Studio</h3><p>No unfamiliar faces, no intimidation — just a space built to nurture growth and connection.</p>
      </div>
      <div class="pillar">
        <svg viewBox="0 0 20 20"><circle cx="10" cy="10" r="7"/><path d="M10 6v4l3 2"/></svg>
        <h3>40-Minute Classes</h3><p>Efficient, full-body sessions that fit into a real schedule — no wasted time.</p>
      </div>
      <div class="pillar">
        <svg viewBox="0 0 20 20"><rect x="3" y="4.5" width="14" height="12" rx="1.5"/><path d="M3 8h14M7 3v3M13 3v3M7.5 12l2 2 3.5-3.5"/></svg>
        <h3>Book in Seconds</h3><p>Browse the live schedule and reserve your spot from your phone in a couple of taps.</p>
      </div>
      <div class="pillar">
        <svg viewBox="0 0 20 20"><circle cx="7.5" cy="7" r="2.7"/><circle cx="13.5" cy="7.5" r="2.2"/><path d="M2.5 16a5 5 0 0 1 10 0M12 12.2a4 4 0 0 1 5.5 3.8"/></svg>
        <h3>Community That Shows Up</h3><p>Clients become regulars, regulars become friends. That's the Quellin difference.</p>
      </div>
    </div>
  </div>
</section>

<section class="studios">
  <div class="wrap">
    <div class="eyebrow">Studios</div>
    <h2>Two studios, one<br>community.</h2>
    <div class="studio-grid">
      <article class="studio">
        <div class="studio-photo one" role="img" aria-label="Group class working out on machines at the Marrow Creek studio"></div>
        <div class="studio-info">
          <div class="eyebrow">Flagship</div>
          <h3>Marrow Creek, TX</h3>
          <small>[Studio address] · Marrow Creek, TX · [Hours]</small>
          <div class="studio-actions"><a class="btn btn-ghost">View schedule</a><span class="link">Get directions →</span></div>
        </div>
      </article>
      <article class="studio">
        <div class="studio-photo two" role="img" aria-label="Instructor leading class at the West Alder studio"></div>
        <div class="studio-info">
          <div class="eyebrow">Now open</div>
          <h3>West Alder, TX</h3>
          <small>[Studio address] · West Alder, TX · [Hours]</small>
          <div class="studio-actions"><a class="btn btn-ghost">View schedule</a><span class="link">Get directions →</span></div>
        </div>
      </article>
    </div>
    <div class="coming"><span class="eyebrow">Coming soon</span><span><b>Pinehollow, TX</b> — Fall 2026</span><span><b>Ashford Bend, TX</b> — Spring 2027</span></div>
  </div>
</section>

<section class="love">
  <div class="wrap">
    <div class="eyebrow">Client love</div>
    <h2>Hear it from the<br>community.</h2>
    <div class="quotes">
      <blockquote class="quote"><div class="mark">“</div><p>Tensa is such a great workout and all of the instructors at Quellin are great! Challenging yet energetic and fun — they're great at ensuring your form is correct in order to prevent injury.</p><cite>MARA T.</cite></blockquote>
      <blockquote class="quote"><div class="mark">“</div><p>Such an intense low impact workout. I immediately felt muscles I never knew I had. Went to my first class with no idea what I was getting into and I've kept going back.</p><cite>NIA B.</cite></blockquote>
      <blockquote class="quote"><div class="mark">“</div><p>I have been loving my experience with Quellin! It is so challenging but the instructors are incredible — patient and encouraging, while still pushing you to dig deeper.</p><cite>JESS R.</cite></blockquote>
    </div>
  </div>
</section>

<section class="social">
  <div class="wrap">
    <div class="social-head">
      <div><div class="eyebrow">Follow along</div><h2>@quellinstudio</h2></div>
      <a class="btn btn-outline">Follow on Instagram</a>
    </div>
    <div class="tiles">
      <div class="tile t1" role="img" aria-label="Instagram post: group photo of members"></div>
      <div class="tile t2" role="img" aria-label="Instagram post: announcement graphic"></div>
      <div class="tile t3" role="img" aria-label="Instagram post: instructor portrait"></div>
      <div class="tile t4" role="img" aria-label="Instagram post: studio interior"></div>
      <div class="tile t5" role="img" aria-label="Instagram post: studio lit in blue"></div>
      <div class="tile t6" role="img" aria-label="Instagram post: client milestones graphic"></div>
    </div>
  </div>
</section>

<section class="newsletter">
  <div class="wrap">
    <div>
      <div class="eyebrow">Join our newsletter</div>
      <h2>Studio news, straight to your inbox.</h2>
      <small>Sign up for updates, offers and new class announcements.</small>
    </div>
    <div class="signup"><div class="field">Email address</div><a class="btn btn-light">Sign up</a></div>
  </div>
</section>

<footer class="footer">
  <div class="wrap">
    <div class="footer-grid">
      <div>
        <span class="brand-name">Quellin</span><span class="brand-tag">Elevated strength.</span>
        <p class="footer-about">A boutique, female-owned Tensa studio in Marrow Creek &amp; West Alder, TX. Elevated strength, for every body.</p>
        <div class="social-icons"><span></span><span></span></div>
      </div>
      <div><h5>EXPLORE</h5><ul><li>Schedule</li><li>Pricing</li><li>The Studio</li><li>Instructors</li><li>Contact</li></ul></div>
      <div><h5>MARROW CREEK, TX</h5><p>[Studio address]<br>Marrow Creek, TX 77501<br>[Phone number]</p></div>
      <div><h5>WEST ALDER, TX</h5><p>[Studio address]<br>West Alder, TX 77502<br>[Phone number]</p></div>
    </div>
    <div class="legal"><span>© 2026 Quellin Tensa. All rights reserved.</span><div><span>Privacy Policy</span><span>Studio Policies</span></div></div>
  </div>
</footer>

</body>
</html>
```